TEK Logistics - Banner 2.5' x 8' for 20+ locations

Need a banner designed that will pop. This banner will be displayed at over 20 of our transportation facilities. Goal is for the banner to grab the attention of employees, contractors and clients and help reinforce our mission and core values. Designed needs to include TEK Logo, our core values and mission statement. Red and Black are the main company colors and we need to stay within that theme and color pallet. Attached is a previous version that was too basic and boring. Willing to consider a design that excludes the mission statement.

Gathering more feedback

```html
<!DOCTYPE html>
<html lang="en">
<head>
<meta charset="utf-8">
<title>TEK Logistics – Mission &amp; Core Values Banner</title>
<link rel="stylesheet" href="https://fonts.googleapis.com/css2?family=Montserrat:wght@600&family=Encode+Sans+Condensed:wght@300&display=swap">
<style>
  :root {
    --page-bg: #4a4848;
    --panel-top: #3b3937;
    --panel-bottom: #2b2a29;
    --brand-red: #b01e24;
    --white: #ffffff;
    --ink: #2b2a29;
    --text-light: #f2f2f2;
    --text-soft: #e3e3e3;
  }
  * { box-sizing: border-box; margin: 0; padding: 0; }
  html, body {
    width: 1200px;
    height: 1200px;
    overflow: hidden;
    background: var(--page-bg);
  }
  .banner {
    position: absolute;
    left: 18px;
    top: 418px;
    width: 1164px;
    height: 364px;
    background: linear-gradient(180deg, var(--panel-top), var(--panel-bottom));
    box-shadow: 0 10px 22px rgba(0,0,0,0.45);
    overflow: hidden;
  }
  .banner__panel {
    position: absolute;
    inset: 0;
    width: 100%;
    height: 100%;
  }
  .brand {
    position: absolute;
    left: 40px;
    top: 160px;
    width: 300px;
    text-align: center;
    color: var(--ink);
    font-family: "Montserrat", sans-serif;
    font-weight: 600;
    font-size: 30px;
    line-height: 40px;
  }
  .mission {
    position: absolute;
    left: 545px;
    top: 30px;
    width: 580px;
    color: var(--text-light);
    font-family: "Montserrat", sans-serif;
    font-weight: 600;
    font-size: 19.5px;
    line-height: 24px;
    letter-spacing: 0.6px;
  }
  .values {
    position: absolute;
    left: 537px;
    top: 166px;
    width: 600px;
    display: grid;
    grid-template-columns: 226px 189px 185px;
    grid-template-rows: 96px 60px;
    list-style: none;
  }
  .value {
    display: flex;
    align-items: flex-start;
    gap: 11px;
    color: var(--text-soft);
    font-family: "Encode Sans Condensed", sans-serif;
    font-weight: 300;
    font-size: 19px;
    line-height: 22px;
  }
  .value__tick {
    flex: none;
    width: 20px;
    height: 20px;
    margin-top: 2px;
  }
</style>
</head>
<body>
  <section class="banner" aria-label="TEK Logistics mission and core values">
    <svg class="banner__panel" viewBox="0 0 1164 364" preserveAspectRatio="none" aria-hidden="true">
      <polygon fill="var(--white)" points="0,0 440,0 370,364 0,364"/>
      <polygon fill="var(--brand-red)" points="440,0 486,0 416,364 370,364"/>
    </svg>

    <p class="brand">TEK Logistics</p>

    <p class="mission">Provide the best customer experience while creating an environment of growth and opportunity for our customers, employees, and service providers.</p>

    <ul class="values">
      <li class="value"><svg class="value__tick" viewBox="0 0 20 20" aria-hidden="true"><circle cx="10" cy="10" r="8.5" fill="none" stroke="#e3e3e3" stroke-width="1.3"/><path d="M6 10.2 L8.8 13 L14 7.4" fill="none" stroke="#e3e3e3" stroke-width="1.4"/></svg><span>Do the right things<br>for the right reasons</span></li>
      <li class="value"><svg class="value__tick" viewBox="0 0 20 20" aria-hidden="true"><circle cx="10" cy="10" r="8.5" fill="none" stroke="#e3e3e3" stroke-width="1.3"/><path d="M6 10.2 L8.8 13 L14 7.4" fill="none" stroke="#e3e3e3" stroke-width="1.4"/></svg><span>Pursue growth<br>and development</span></li>
      <li class="value"><svg class="value__tick" viewBox="0 0 20 20" aria-hidden="true"><circle cx="10" cy="10" r="8.5" fill="none" stroke="#e3e3e3" stroke-width="1.3"/><path d="M6 10.2 L8.8 13 L14 7.4" fill="none" stroke="#e3e3e3" stroke-width="1.4"/></svg><span>Build a positive<br>team atmosphere</span></li>
      <li class="value"><svg class="value__tick" viewBox="0 0 20 20" aria-hidden="true"><circle cx="10" cy="10" r="8.5" fill="none" stroke="#e3e3e3" stroke-width="1.3"/><path d="M6 10.2 L8.8 13 L14 7.4" fill="none" stroke="#e3e3e3" stroke-width="1.4"/></svg><span>Deliver WOW<br>through service</span></li>
      <li class="value"><svg class="value__tick" viewBox="0 0 20 20" aria-hidden="true"><circle cx="10" cy="10" r="8.5" fill="none" stroke="#e3e3e3" stroke-width="1.3"/><path d="M6 10.2 L8.8 13 L14 7.4" fill="none" stroke="#e3e3e3" stroke-width="1.4"/></svg><span>Do everything<br>Safely</span></li>
      <li class="value"><svg class="value__tick" viewBox="0 0 20 20" aria-hidden="true"><circle cx="10" cy="10" r="8.5" fill="none" stroke="#e3e3e3" stroke-width="1.3"/><path d="M6 10.2 L8.8 13 L14 7.4" fill="none" stroke="#e3e3e3" stroke-width="1.4"/></svg><span>Have Fun</span></li>
    </ul>
  </section>
</body>
</html>
```